K8 FIRST WEBSITE FOR CONCRETE DESIGN START-UP

We would like a 3-4 page website. Very basic. About Us, Pricing, Testimonials, Pictures and somewhere they can contact us. We are a concrete design/epoxy company. Want clean/modern and something that is user friendly that we can keep building on. Important we can update the website and that it shows good examples of our work.
Target Market(s)
Home owners or business owners who want unique solutions to concrete flooring in garages, patios, basements, showrooms or anywhere concrete is or can be.
Industry/Entity Type
Concrete
Coding
Coded - Design and coding required
Number of Pages Required
4 page
Look and feel

```html
<!DOCTYPE html>
<html lang="en">
<head>
<meta charset="utf-8">
<title>K8 Concrete</title>
<link href="https://fonts.googleapis.com/css2?family=Audiowide&family=Montserrat:wght@600;700&family=Roboto:wght@400;500;700&display=swap" rel="stylesheet">
<style>
:root{
  --orange:#f0801f;
  --orange-light:#f6a55a;
  --dark:#111111;
  --text:#555555;
  --heading:#1a1a1a;
  --band:#eef0f3;
  --footer:#1c1c1c;
  --white:#ffffff;
}
*{box-sizing:border-box;margin:0;padding:0}
html,body{width:1200px;height:4535px;overflow:hidden}
body{position:relative;background:var(--white);font-family:'Roboto',sans-serif;color:var(--text)}
.abs{position:absolute}
.display{font-family:'Audiowide',sans-serif;color:var(--heading)}

/* header */
.topbar{left:378px;top:0;width:822px;height:46px}
.topbar-text{top:0;height:46px;line-height:46px;color:var(--white);font-size:15px}
.logo{left:130px;top:28px;display:flex;align-items:center;gap:10px;font-family:'Audiowide',sans-serif;font-size:34px;color:var(--heading)}
.logo-mark{width:22px;height:22px;background:var(--orange)}
.nav{left:440px;top:74px;display:flex;gap:37px;font-family:'Montserrat',sans-serif;font-weight:700;font-size:14px;color:var(--dark)}
.nav .active{color:var(--orange)}

/* hero */
.hero{left:0;top:120px;width:1200px;height:625px;background:linear-gradient(180deg,#e3e3e3 0%,#cfcfcf 45%,#5b5b5b 80%,#2b2b2b 100%)}
.hero-box{left:304px;top:300px;width:592px;height:255px;background:rgba(90,90,90,.72);text-align:center;color:var(--white)}
.hero-box h1{font-family:'Audiowide',sans-serif;font-weight:400;font-size:48px;margin-top:28px;color:var(--white)}
.hero-box p{font-size:18px;line-height:34px;margin:8px auto 0;width:480px}
.btn{display:inline-block;background:var(--orange);color:var(--white);font-family:'Audiowide',sans-serif;font-size:17px;padding:9px 30px;clip-path:polygon(10% 0,100% 0,90% 100%,0 100%)}
.arrow-btn{width:52px;height:52px;border-radius:50%;background:var(--white);display:flex;align-items:center;justify-content:center}

/* about */
.about-title{left:110px;top:836px;font-size:31px}
.rule{display:inline-block;width:55px;height:4px;background:var(--orange);vertical-align:middle;margin-left:6px}
.about-text{left:110px;top:884px;width:445px;font-size:14.5px;line-height:28px}
.about-photo{left:665px;top:840px;width:428px;height:308px}

/* section headings */
.section-title{width:1200px;left:0;text-align:center;font-size:31px}
.section-rule{left:572px;width:56px;height:4px;background:var(--orange)}

/* services */
.service-img{width:296px;height:215px;border:3px solid var(--white);box-shadow:0 2px 6px rgba(0,0,0,.25)}
.service-name{font-size:22px}
.service-text{font-size:14.5px;line-height:28px}
.read-more{font-family:'Audiowide',sans-serif;color:var(--orange);font-size:17px}
.service-feature{left:452px;top:1463px;width:296px;height:382px;background:var(--orange);box-shadow:0 6px 14px rgba(0,0,0,.25);text-align:center;color:var(--white)}

/* pricing */
.price-card{width:254px;height:325px;background:var(--white);border:2px solid var(--orange-light)}
.price-card.raised{box-shadow:0 8px 16px rgba(0,0,0,.2)}
.price-head{position:absolute;left:0;top:0;width:250px;height:140px}
.plan-name{position:absolute;left:24px;top:20px;font-family:'Audiowide',sans-serif;color:var(--white);font-size:22px}
.plan-price{position:absolute;left:32px;top:58px;font-family:'Audiowide',sans-serif;color:var(--orange);font-size:40px}
.raised .plan-price{color:var(--dark)}
.plan-period{position:absolute;left:36px;top:146px;font-size:17px;font-weight:500;color:var(--heading)}
.plan-list{position:absolute;left:32px;top:186px;list-style:none;font-size:15px;color:var(--heading)}
.plan-list li{display:flex;align-items:center;gap:14px;height:47px}

/* testimonials */
.quote{width:290px;padding-left:28px;border-left:3px solid var(--orange);font-size:14.5px;line-height:28px;color:#777}
.avatar{width:130px;height:130px;border-radius:50%;background:linear-gradient(135deg,#cfcfcf,#6e6e6e)}
.badge{width:26px;height:26px;background:var(--orange);border-radius:4px;color:var(--white);font-size:22px;font-weight:700;text-align:center;line-height:30px}
.person{font-size:14px;font-weight:700;color:var(--heading)}
.role{font-size:14px;color:#777}
.dot{width:12px;height:12px;border-radius:50%;background:#aaa}

/* gallery */
.tile{width:288px;height:288px}

/* contact */
.contact-photo{left:0;top:3880px;width:600px;height:572px;background:linear-gradient(160deg,#c7a37a 0%,#e6e2dc 40%,#6a6a6a 100%)}
.contact-panel{left:600px;top:3880px;width:600px;height:572px;background:linear-gradient(180deg,#c89870 0%,#ea9a4f 60%,#f08a2a 100%)}
.field{border-bottom:1px solid rgba(255,255,255,.8);color:var(--white);font-size:15px;padding-left:6px;height:30px}
.submit{left:650px;top:4310px;width:128px;height:34px;background:var(--dark);color:var(--white);font-family:'Audiowide',sans-serif;font-size:15px;text-align:center;line-height:34px}
.footer{left:0;top:4452px;width:1200px;height:83px;background:var(--footer);color:var(--white);font-size:14px;text-align:center;line-height:83px}
</style>
</head>
<body>

<!-- Header -->
<svg class="abs topbar" viewBox="0 0 822 46" aria-hidden="true"><polygon points="0,0 822,0 822,46 42,46" fill="#f0801f"/><polygon points="508,0 546,0 546,46 508,46" fill="#fff"/></svg>
<div class="abs topbar-text" style="left:458px">&#9993;&nbsp; info@k8concrete.com</div>
<div class="abs topbar-text" style="left:776px">Call us Today</div>
<svg class="abs" style="left:897px;top:14px" width="18" height="18" viewBox="0 0 24 24"><path d="M6.6 10.8a15 15 0 0 0 6.6 6.6l2.2-2.2c.3-.3.7-.4 1-.2 1.1.4 2.3.6 3.6.6.6 0 1 .4 1 1V20c0 .6-.4 1-1 1A17 17 0 0 1 3 4c0-.6.4-1 1-1h3.5c.6 0 1 .4 1 1 0 1.3.2 2.5.6 3.6.1.3 0 .7-.2 1z" fill="#f0801f"/></svg>
<div class="abs topbar-text" style="left:932px;font-weight:700;font-size:19px">+1 555 010 0199</div>
<div class="abs logo"><span class="logo-mark"></span>K8</div>
<nav class="abs nav"><span class="active">HOME</span><span>ABOUT US</span><span>PRICING</span><span>TESTIMONIALS</span><span>GALLERY</span><span>CONTACT US</span></nav>
<div class="abs" style="left:0;top:119px;width:1200px;height:1px;background:#ddd"></div>

<!-- Hero -->
<div class="abs hero" role="img" aria-label="Photo of a modern bedroom with a marble wall and polished concrete floor"></div>
<div class="abs arrow-btn" style="left:38px;top:424px"><svg width="18" height="18" viewBox="0 0 24 24"><path d="M15 4 7 12l8 8" stroke="#333" stroke-width="2.4" fill="none"/></svg></div>
<div class="abs arrow-btn" style="left:1118px;top:424px"><svg width="18" height="18" viewBox="0 0 24 24"><path d="m9 4 8 8-8 8" stroke="#333" stroke-width="2.4" fill="none"/></svg></div>
<div class="abs hero-box">
  <h1>K8 CONCRETE</h1>
  <p>Lorem ipsum dolor sit amet, consectetur adipiscing elit, sed do eiusmod tempor incididunt ut labore</p>
  <span class="btn" style="margin-top:14px">GET STARTED</span>
</div>

<!-- About -->
<h2 class="abs display about-title">ABOUT K8 CONCRETE<span class="rule"></span></h2>
<p class="abs about-text">Sed ut perspiciatis unde omnis iste natus error sit voluptatem accusantium doloremque laudantium, totam rem aperiam, eaque ipsa quae ab illo inventore veritatis et quasi architecto beatae vitae dicta sunt explicabo. Nemo enim ipsam voluptatem quia voluptas sit aspernatur aut odit aut fugit, sed quia consequuntur magni dolores eos qui ratione</p>
<span class="abs btn" style="left:110px;top:1070px">READ MORE &#8853;</span>
<svg class="abs about-photo" viewBox="0 0 428 308" role="img" aria-label="Photo of a worker polishing a concrete floor with an orange machine">
  <defs><linearGradient id="ap" x1="0" y1="0" x2="0" y2="1"><stop offset="0" stop-color="#c9c4bc"/><stop offset="1" stop-color="#6f747a"/></linearGradient></defs>
  <polygon points="0,0 50,0 30,200" fill="#f6a55a"/>
  <polygon points="428,308 380,308 400,110" fill="#f6a55a"/>
  <polygon points="20,0 428,0 408,308 0,308" fill="url(#ap)"/>
</svg>

<!-- Services -->
<svg class="abs" style="left:0;top:1250px" width="1200" height="716" viewBox="0 0 1200 716" aria-hidden="true"><polygon points="0,45 1200,0 1200,670 0,716" fill="#dfe3e8"/></svg>
<h2 class="abs display section-title" style="top:1367px">OUR SERVICES</h2>
<div class="abs section-rule" style="top:1419px"></div>
<div class="abs" style="left:40px;top:1652px"><svg width="34" height="34" viewBox="0 0 34 34"><circle cx="17" cy="17" r="15" fill="none" stroke="#111" stroke-width="3"/><path d="M20 10 13 17l7 7M13 17h11" stroke="#111" stroke-width="3" fill="none"/></svg></div>
<div class="abs" style="left:1126px;top:1652px"><svg width="34" height="34" viewBox="0 0 34 34"><circle cx="17" cy="17" r="15" fill="none" stroke="#111" stroke-width="3"/><path d="m14 10 7 7-7 7M21 17H10" stroke="#111" stroke-width="3" fill="none"/></svg></div>

<div class="abs service-img" style="left:110px;top:1463px;background:linear-gradient(160deg,#f2f2f2,#c8c8c8)" role="img" aria-label="Photo of a concrete polishing machine on a grey floor"></div>
<div class="abs display service-name" style="left:110px;top:1692px">Concrete Polishing</div>
<p class="abs service-text" style="left:110px;top:1728px;width:290px">Concrete polishing is a task best performed by a professional who knows</p>
<div class="abs read-more" style="left:110px;top:1797px">READ MORE &#8853;</div>

<div class="abs service-feature">
  <div style="font-family:'Audiowide',sans-serif;font-size:22px;line-height:35px;margin-top:40px">Concrete<br>Resurfacing</div>
  <p style="font-size:14.5px;line-height:28px;margin:12px 16px 0">Concrete polishing is a task best performed by a professional who knows Your concrete has seen better days. When it was new, it looked great but now it's an eyesore that detracts from your curb appeal.</p>
  <div style="font-family:'Audiowide',sans-serif;font-size:17px;margin-top:22px">READ MORE &#8853;</div>
</div>

<div class="abs service-img" style="left:793px;top:1463px;background:linear-gradient(180deg,#8f8a82,#c9d4de)" role="img" aria-label="Photo of two workers spreading epoxy on a floor"></div>
<div class="abs display service-name" style="left:793px;top:1692px">EPOXY FLOORING</div>
<p class="abs service-text" style="left:793px;top:1728px;width:290px">Concrete polishing is a task best performed by a professional who knows</p>
<div class="abs read-more" style="left:793px;top:1797px">READ MORE &#8853;</div>

<!-- Pricing -->
<h2 class="abs display section-title" style="top:2050px">OUR PRICING</h2>
<div class="abs section-rule" style="top:2100px"></div>

<div class="abs price-card" style="left:126px;top:2150px">
  <svg class="price-head" viewBox="0 0 250 140" aria-hidden="true"><polygon points="0,0 250,0 250,10 62,140 0,140" fill="#111"/></svg>
  <div class="plan-name">BASE COAT</div><div class="plan-price">$99</div>
  <div class="plan-period">PRICE MONTH</div>
  <ul class="plan-list"><li><svg width="20" height="20" viewBox="0 0 20 20"><circle cx="10" cy="10" r="10" fill="#f0801f"/><path d="m5.5 10 3 3 6-6" stroke="#fff" stroke-width="2.2" fill="none"/></svg>Motivation Lecturer</li><li><svg width="20" height="20" viewBox="0 0 20 20"><circle cx="10" cy="10" r="10" fill="#f0801f"/><path d="m5.5 10 3 3 6-6" stroke="#fff" stroke-width="2.2" fill="none"/></svg>Success Expert</li><li><svg width="20" height="20" viewBox="0 0 20 20"><circle cx="10" cy="10" r="10" fill="#f0801f"/><path d="m5.5 10 3 3 6-6" stroke="#fff" stroke-width="2.2" fill="none"/></svg>Leadership Lead You</li></ul>
</div>

<div class="abs price-card raised" style="left:472px;top:2150px">
  <svg class="price-head" viewBox="0 0 250 140" aria-hidden="true"><polygon points="0,0 250,0 250,10 62,140 0,140" fill="#f0801f"/></svg>
  <div class="plan-name">BASE COAT</div><div class="plan-price">$99</div>
  <div class="plan-period">PRICE MONTH</div>
  <ul class="plan-list"><li><svg width="20" height="20" viewBox="0 0 20 20"><circle cx="10" cy="10" r="10" fill="#f0801f"/><path d="m5.5 10 3 3 6-6" stroke="#fff" stroke-width="2.2" fill="none"/></svg>Motivation Lecturer</li><li><svg width="20" height="20" viewBox="0 0 20 20"><circle cx="10" cy="10" r="10" fill="#f0801f"/><path d="m5.5 10 3 3 6-6" stroke="#fff" stroke-width="2.2" fill="none"/></svg>Success Expert</li><li><svg width="20" height="20" viewBox="0 0 20 20"><circle cx="10" cy="10" r="10" fill="#f0801f"/><path d="m5.5 10 3 3 6-6" stroke="#fff" stroke-width="2.2" fill="none"/></svg>Leadership Lead You</li></ul>
</div>

<div class="abs price-card" style="left:818px;top:2150px">
  <svg class="price-head" viewBox="0 0 250 140" aria-hidden="true"><polygon points="0,0 250,0 250,10 62,140 0,140" fill="#111"/></svg>
  <div class="plan-name">BASE COAT</div><div class="plan-price">$99</div>
  <div class="plan-period">PRICE MONTH</div>
  <ul class="plan-list"><li><svg width="20" height="20" viewBox="0 0 20 20"><circle cx="10" cy="10" r="10" fill="#f0801f"/><path d="m5.5 10 3 3 6-6" stroke="#fff" stroke-width="2.2" fill="none"/></svg>Motivation Lecturer</li><li><svg width="20" height="20" viewBox="0 0 20 20"><circle cx="10" cy="10" r="10" fill="#f0801f"/><path d="m5.5 10 3 3 6-6" stroke="#fff" stroke-width="2.2" fill="none"/></svg>Success Expert</li><li><svg width="20" height="20" viewBox="0 0 20 20"><circle cx="10" cy="10" r="10" fill="#f0801f"/><path d="m5.5 10 3 3 6-6" stroke="#fff" stroke-width="2.2" fill="none"/></svg>Leadership Lead You</li></ul>
</div>

<!-- Testimonials -->
<svg class="abs" style="left:0;top:2520px" width="1200" height="690" viewBox="0 0 1200 690" aria-hidden="true"><polygon points="0,45 1200,0 1200,690 0,690" fill="#f0f0f2"/></svg>
<h2 class="abs display section-title" style="top:2707px">OUR TESTIMONIALS</h2>
<div class="abs section-rule" style="top:2770px"></div>

<p class="abs quote" style="left:108px;top:2830px">Lorem Ipsum is simply dummy text of the printing &amp; typesetting industry. Lorem scrambled it to type specimen book.</p>
<p class="abs quote" style="left:450px;top:2830px">Lorem Ipsum is simply dummy text of the printing &amp; typesetting industry. Lorem scrambled it to type specimen book.</p>
<p class="abs quote" style="left:792px;top:2830px">Lorem Ipsum is simply dummy text of the printing &amp; typesetting industry. Lorem scrambled it to type specimen book.</p>

<div class="abs avatar" style="left:112px;top:2970px" role="img" aria-label="Customer portrait"></div>
<div class="abs badge" style="left:210px;top:3060px">&#8220;</div>
<div class="abs person" style="left:272px;top:3010px">Mark Ellis</div><div class="abs role" style="left:274px;top:3046px">Customer</div>

<div class="abs avatar" style="left:454px;top:2970px" role="img" aria-label="Customer portrait"></div>
<div class="abs badge" style="left:552px;top:3060px">&#8220;</div>
<div class="abs person" style="left:614px;top:3010px">Ryan Cole</div><div class="abs role" style="left:616px;top:3046px">Customer</div>

<div class="abs avatar" style="left:796px;top:2970px" role="img" aria-label="Customer portrait"></div>
<div class="abs badge" style="left:894px;top:3060px">&#8220;</div>
<div class="abs person" style="left:956px;top:3010px">Victor Hale</div><div class="abs role" style="left:958px;top:3046px">Customer</div>

<div class="abs dot" style="left:562px;top:3186px;background:var(--orange)"></div>
<div class="abs dot" style="left:578px;top:3186px"></div>
<div class="abs dot" style="left:594px;top:3186px"></div>
<div class="abs dot" style="left:610px;top:3186px"></div>
<div class="abs dot" style="left:626px;top:3186px"></div>

<!-- Gallery -->
<div class="abs tile" style="left:2px;top:3273px;background:linear-gradient(135deg,#a9aaa8,#6f7170)" role="img" aria-label="Photo of a curved concrete wall"></div>
<div class="abs tile" style="left:305px;top:3273px;background:linear-gradient(135deg,#f3a660,#e88a3a)" role="img" aria-label="Photo of a warm lit interior with concrete floor"></div>
<div class="abs" style="left:420px;top:3388px;width:58px;height:58px;background:var(--orange);display:flex;align-items:center;justify-content:center"><svg width="24" height="22" viewBox="0 0 24 22"><path d="M12 21 2.5 11.5A5.5 5.5 0 0 1 12 4a5.5 5.5 0 0 1 9.5 7.5z" fill="#fff"/></svg></div>
<div class="abs tile" style="left:608px;top:3273px;background:linear-gradient(180deg,#d9d9d9,#5e5e5e)" role="img" aria-label="Photo of a modern room with dark concrete walls"></div>
<div class="abs tile" style="left:911px;top:3273px;background:linear-gradient(180deg,#c2c8cc,#8d9499)" role="img" aria-label="Photo of a glass hall with a polished floor"></div>
<div class="abs tile" style="left:2px;top:3577px;background:linear-gradient(180deg,#eef0f3,#bfc4c9)" role="img" aria-label="Photo of a bright white corridor"></div>
<div class="abs tile" style="left:305px;top:3577px;background:linear-gradient(180deg,#e9e9e9,#b5b5b5)" role="img" aria-label="Photo of a kitchen and dining area with concrete floor"></div>
<div class="abs tile" style="left:608px;top:3577px;background:linear-gradient(180deg,#f1f1f1,#a9a9a9)" role="img" aria-label="Photo of an open living space with polished floor"></div>
<div class="abs tile" style="left:911px;top:3577px;background:linear-gradient(135deg,#b8b8b6,#9a9b9b)" role="img" aria-label="Photo of a speckled epoxy floor finish"></div>

<!-- Contact -->
<div class="abs contact-photo" role="img" aria-label="Photo of a worker operating a concrete spraying machine"></div>
<div class="abs contact-panel"></div>
<h2 class="abs display" style="left:645px;top:3987px;font-size:29px;color:var(--white);font-weight:400">GET IN TOUCH</h2>
<div class="abs field" style="left:648px;top:4083px;width:210px">First Name</div>
<div class="abs field" style="left:873px;top:4083px;width:215px">Last Name</div>
<div class="abs field" style="left:648px;top:4143px;width:210px">Date</div>
<div class="abs field" style="left:873px;top:4143px;width:100px">Time</div>
<div class="abs field" style="left:992px;top:4143px;width:96px">Phone</div>
<div class="abs field" style="left:648px;top:4209px;width:440px">Message</div>
<div class="abs submit">SUBMIT</div>

<!-- Footer -->
<div class="abs footer">&copy; Copyrights 2019 | K8 Concrete</div>

</body>
</html>
```